Graphic Design for Ledgerwave Forum Event

We are looking for up to 15 hi-tech image designs for use in advertising our cryptocurrency/blockchain event (www.ledgerwaveforum.example) online. Designs to be 1200 x 628

We will be using these images for online advertising of our summit and preference will be given to those with eye catching and clean designs.

Target Market(s)

Corporate CEO’s, CTO’s & CIO’s
Managing Director’s & VP’s
Blockchain Startups
Social Entrepreneurs
Technology Futurists
Attorney’s & Securities Lawyers
Blockchain Developers
FinTech Execs
ICO Advisors/Consultant’s
VC’s/Investors

Industry/Entity Type

Information Technology

Font styles to use
Sans Serif

Colors

Designer to choose colors to be used in the design.

Requirements
Must have
• Eye catching designs relating to the blockchain and cryptocurrency industries
Nice to have
• Suggested copy for ads would be nice
Should not have
• Please keep focused on industry.

```html
<!DOCTYPE html>
<html lang="en">
<head>
<meta charset="utf-8">
<title>Ledgerwave Forum – Bringing Thought Leaders To You</title>
<link rel="stylesheet" href="https://fonts.googleapis.com/css2?family=Poppins:wght@300;400;500;700&display=swap">
<style>
  :root {
    --ink: #121214;
    --ink-soft: #1b1b1f;
    --orange: #f7941d;
    --red-orange: #f15a29;
    --slate: #3b3b3e;
    --white: #ffffff;
    --muted: #c9c9c9;
    --net-night: #041a3f;
    --net-deep: #0a3a7a;
    --net-mid: #1a73c9;
    --net-glow: #bfe8ff;
  }
  * { margin: 0; padding: 0; box-sizing: border-box; }
  html, body { width: 1200px; height: 628px; overflow: hidden; background: var(--ink); }
  body { font-family: "Poppins", Arial, sans-serif; color: var(--white); }

  .ad { position: relative; width: 1200px; height: 628px; overflow: hidden; background: var(--ink); }
  .shapes { position: absolute; inset: 0; }

  .event-title { position: absolute; left: 0; width: 672px; top: 70px; text-align: center;
                 font-weight: 700; font-size: 48px; line-height: 1.2; color: var(--red-orange);
                 letter-spacing: -0.5px; }
  .tagline { position: absolute; left: 0; width: 668px; top: 143px; text-align: center;
             font-weight: 300; font-size: 27px; line-height: 1.2; color: var(--white); }

  .brand { position: absolute; right: 40px; top: 62px; display: flex; align-items: center; gap: 8px;
           font-weight: 500; font-size: 15px; color: var(--white); }
  .brand-dot { width: 12px; height: 12px; border-radius: 50%; background: var(--white); }

  .speaker { position: absolute; top: 395px; width: 220px; text-align: center; }
  .speaker-photo { width: 112px; height: 112px; margin: 0 auto; border-radius: 50%;
                   border: 2px solid var(--white);
                   background: linear-gradient(160deg, #e2e2e2, #8a8a8a); }
  .speaker-name { margin-top: 13px; font-size: 11.5px; line-height: 1.2; font-weight: 500;
                  letter-spacing: 1.6px; text-transform: uppercase; white-space: nowrap; }
  .speaker-role { margin-top: 7px; font-size: 9px; line-height: 1.2; color: var(--muted); white-space: nowrap; }

  .info-bar { position: absolute; left: 0; bottom: 0; height: 50px; width: 580px; font-size: 18px;
              letter-spacing: 0.3px; }
  .info-item { position: absolute; top: 0; height: 50px; display: flex; align-items: center; gap: 16px; }
  .info-date { left: 98px; }
  .info-place { left: 341px; gap: 14px; }
</style>
</head>
<body>
<main class="ad">
  <svg class="shapes" width="1200" height="628" viewBox="0 0 1200 628">
    <defs>
      <linearGradient id="network-sky" x1="0" y1="0" x2="0" y2="1">
        <stop offset="0" stop-color="var(--net-night)"/>
        <stop offset="0.3" stop-color="var(--net-deep)"/>
        <stop offset="0.42" stop-color="var(--net-mid)"/>
        <stop offset="1" stop-color="var(--net-deep)"/>
      </linearGradient>
      <radialGradient id="network-horizon" cx="940" cy="760" r="560" gradientUnits="userSpaceOnUse">
        <stop offset="0" stop-color="var(--net-mid)" stop-opacity="0.2"/>
        <stop offset="0.8" stop-color="var(--net-mid)" stop-opacity="0.6"/>
        <stop offset="0.94" stop-color="var(--net-glow)" stop-opacity="0.85"/>
        <stop offset="1" stop-color="var(--net-glow)" stop-opacity="0"/>
      </radialGradient>
    </defs>
    <g class="network-visual" role="img" aria-label="Glowing blue globe seen from orbit, covered in a blockchain network of linked nodes with beams of light rising from it">
      <rect x="560" y="0" width="640" height="628" fill="url(#network-sky)"/>
      <rect x="560" y="0" width="640" height="628" fill="url(#network-horizon)"/>
    </g>
    <polygon class="dark-field" points="0,0 712,0 518,360 640,628 0,628" fill="var(--ink)"/>
    <polygon class="chevron-upper" points="712,0 872,0 686,360 518,360" fill="var(--orange)"/>
    <polygon class="chevron-lower" points="518,360 686,360 820,628 640,628" fill="var(--red-orange)"/>
    <polygon class="chevron-shadow" points="513,628 598,496 656,628" fill="var(--slate)"/>
    <rect class="info-band" x="0" y="578" width="545" height="50" fill="var(--red-orange)"/>

    <g class="speaker-bracket" stroke="var(--muted)" stroke-width="1.4" fill="none">
      <polyline points="116,382 116,362 276,362"/>
      <polyline points="306,362 464,362 464,382"/>
    </g>
    <g class="mic-icon" fill="none" stroke="var(--red-orange)" stroke-width="2.2" stroke-linecap="round">
      <rect x="286" y="343" width="10" height="19" rx="5" fill="var(--red-orange)"/>
      <path d="M281 356 a10 10 0 0 0 20 0"/>
      <line x1="291" y1="366" x2="291" y2="374"/>
    </g>
  </svg>

  <h1 class="event-title">Ledgerwave Forum</h1>
  <p class="tagline">Bringing Thought Leaders To You</p>

  <div class="brand"><span class="brand-dot"></span>Ledgerwave Forum</div>

  <section class="speakers">
    <div class="speaker" style="left:6px">
      <div class="speaker-photo" role="img" aria-label="Portrait photo of speaker Reid Tanaka"></div>
      <p class="speaker-name">Reid Tanaka</p>
      <p class="speaker-role">ICO Advisor &amp; Investor</p>
    </div>
    <div class="speaker" style="left:180px">
      <div class="speaker-photo" role="img" aria-label="Portrait photo of speaker Elena Varga"></div>
      <p class="speaker-name">Elena Varga, Ph.D.</p>
      <p class="speaker-role">CEO of Harborline Capital Group</p>
    </div>
    <div class="speaker" style="left:352px">
      <div class="speaker-photo" role="img" aria-label="Portrait photo of speaker Wen Liang"></div>
      <p class="speaker-name">Wen Liang</p>
      <p class="speaker-role">Fin Tench Thought Leader</p>
    </div>
  </section>

  <footer class="info-bar">
    <div class="info-item info-date">
      <svg width="20" height="20" viewBox="0 0 20 20" fill="none" stroke="var(--white)" stroke-width="2">
        <rect x="2" y="4" width="16" height="14" rx="1.5"/>
        <line x1="2" y1="8.5" x2="18" y2="8.5"/>
        <line x1="6" y1="1.5" x2="6" y2="5.5"/><line x1="14" y1="1.5" x2="14" y2="5.5"/>
      </svg>
      <span>28/29 MARCH 2018</span>
    </div>
    <div class="info-item info-place">
      <svg width="16" height="22" viewBox="0 0 16 22">
        <path d="M8 0a8 8 0 0 0-8 8c0 6 8 14 8 14s8-8 8-14a8 8 0 0 0-8-8z" fill="var(--white)"/>
        <circle cx="8" cy="8" r="3" fill="var(--red-orange)"/>
      </svg>
      <span>TAMPA,FL</span>
    </div>
  </footer>
</main>
</body>
</html>
```